Business Card Design for a Lending Business (Hard Money loans)

We need a business card for our Real Estate Lending business. We do hard Money loans for real estate investors. We have an existing logo we like, see attached. I'd like the business card to mostly include the logo colors, but a bright color pop of some sort would be nice to see also. Card should include Logo, Company Name, Company Address, Employee Name, Cell Phone, Main Phone, Email, Website

Industry/Entity Type

Finance / Lending

Contact Information for Business Card

Logo, Company Name, Company Address, Employee Name, Cell Phone, Main Phone, Email, Website

Requirements
Nice to have
• I'd like the business card to mostly include the logo colors, but a bright color pop of some sort would be nice to see also.

```html
<!DOCTYPE html>
<html lang="en">
<head>
<meta charset="utf-8">
<title>Harborline Capital – Business Card</title>
<link rel="stylesheet" href="https://fonts.googleapis.com/css2?family=Montserrat:wght@400;500;700;800&display=swap">
<style>
  :root {
    --backdrop: #3a3a3c;
    --card-white: #ffffff;
    --card-fade: #f2f2f2;
    --navy: #0a1f80;
    --navy-deep: #031565;
    --royal: #1a37a0;
    --cyan: #1ab4e6;
    --ink: #1a1a1a;
  }
  * { margin: 0; padding: 0; box-sizing: border-box; }
  html, body {
    width: 1200px; height: 1200px; overflow: hidden;
    background: var(--backdrop);
    font-family: "Montserrat", sans-serif;
  }
  .stage {
    position: relative; width: 1200px; height: 1200px;
    display: flex; flex-direction: column; align-items: center; justify-content: center; gap: 56px;
  }
  .card {
    position: relative; width: 880px; height: 503px;
    border-radius: 34px; overflow: hidden;
    box-shadow: 0 14px 30px rgba(0,0,0,.45);
  }
  .card-front { background: linear-gradient(180deg, var(--card-white) 55%, var(--card-fade)); }
  .card-back { background: radial-gradient(ellipse at 50% 45%, var(--navy) 0%, var(--navy-deep) 80%); }

  .front-bands { position: absolute; left: 0; bottom: 0; width: 880px; height: 503px; }

  .identity { position: absolute; left: 64px; top: 250px; color: var(--ink); }
  .identity .full-name { font-weight: 800; font-size: 34px; color: var(--cyan); letter-spacing: -0.5px; line-height: 1; }
  .identity .position { font-weight: 500; font-size: 17px; margin-top: 6px; letter-spacing: .5px; }
  .contact-list { list-style: none; margin-top: 16px; }
  .contact-list li { display: flex; align-items: center; gap: 14px; font-size: 19px; font-weight: 500; height: 32px; }
  .contact-list svg { width: 22px; height: 22px; flex: none; }

  .brand { display: flex; align-items: center; gap: 16px; }
  .brand .brand-dot { border-radius: 50%; flex: none; }
  .brand .brand-name { font-weight: 800; letter-spacing: 2px; line-height: 1; }

  .front-brand { position: absolute; right: 70px; top: 150px; }
  .front-brand .brand-dot { width: 46px; height: 46px; background: var(--navy); }
  .front-brand .brand-name { font-size: 34px; color: var(--navy); }

  .back-brand { position: absolute; left: 50%; top: 50%; transform: translate(-50%, -50%); }
  .back-brand .brand-dot { width: 60px; height: 60px; background: var(--cyan); }
  .back-brand .brand-name { font-size: 48px; color: var(--card-white); }
</style>
</head>
<body>
<main class="stage">
  <section class="card card-front" aria-label="Card front">
    <svg class="front-bands" viewBox="0 0 880 503" aria-hidden="true">
      <polygon points="0,495 505,455 505,503 0,503" fill="var(--cyan)"/>
      <polygon points="520,418 880,395 880,503 520,503" fill="var(--royal)"/>
      <polygon points="520,418 880,395 880,420 520,440" fill="var(--navy)"/>
    </svg>

    <div class="front-brand brand">
      <span class="brand-dot"></span>
      <span class="brand-name">HARBORLINE CAPITAL</span>
    </div>

    <div class="identity">
      <p class="full-name">FULL NAME</p>
      <p class="position">POSITION</p>
      <ul class="contact-list">
        <li>
          <svg viewBox="0 0 24 24"><rect x="7" y="2" width="10" height="20" rx="2" fill="none" stroke="var(--cyan)" stroke-width="2"/><circle cx="12" cy="18.5" r="1" fill="var(--cyan)"/></svg>
          <span>(000) 000 0000</span>
        </li>
        <li>
          <svg viewBox="0 0 24 24"><path d="M6.6 10.8a15 15 0 0 0 6.6 6.6l2.2-2.2a1 1 0 0 1 1-.25 11.4 11.4 0 0 0 3.6.57 1 1 0 0 1 1 1V20a1 1 0 0 1-1 1A17 17 0 0 1 3 4a1 1 0 0 1 1-1h3.5a1 1 0 0 1 1 1c0 1.25.2 2.45.57 3.57a1 1 0 0 1-.25 1z" fill="var(--cyan)"/></svg>
          <span>(000) 000 0000</span>
        </li>
        <li>
          <svg viewBox="0 0 24 24"><rect x="2" y="5" width="20" height="14" fill="var(--cyan)"/><path d="M2 5l10 8 10-8" fill="none" stroke="#fff" stroke-width="1.6"/></svg>
          <span>email@company.com</span>
        </li>
        <li>
          <svg viewBox="0 0 24 24"><circle cx="12" cy="12" r="9.5" fill="none" stroke="var(--cyan)" stroke-width="2"/><ellipse cx="12" cy="12" rx="4" ry="9.5" fill="none" stroke="var(--cyan)" stroke-width="1.6"/><path d="M2.5 12h19M4 7h16M4 17h16" stroke="var(--cyan)" stroke-width="1.6"/></svg>
          <span>www.company.com</span>
        </li>
      </ul>
    </div>
  </section>

  <section class="card card-back" aria-label="Card back">
    <div class="back-brand brand">
      <span class="brand-dot"></span>
      <span class="brand-name">HARBORLINE CAPITAL</span>
    </div>
  </section>
</main>
</body>
</html>
```